Country Duo act needs single artwork

We need artwork for our latest single for tunorra and other music streaming sites. The design can include the pictures in the attached files that we uploaded but we are also open to designs that also don't include them. It should be easy to read the song title
"Rain Won't Wait" and our band name Orchard 19 - this track is our actual story. Must be at least 640 x 640 pixels to be acceptable to tunorra. We have also included a copy of the track for inspiration.
Check us out on tunorra to see other artwork -> https://play.tunorra.net/artist/8QkTbnR4wXe71PuzMdGhVc?si=Hq3LmPa-Tb9Wn2KcXoRvEd

Target Market(s)

Country music fans

Industry/Entity Type

Music

Font styles to use
Decorative

Colors

Designer to choose colors to be used in the design.

Requirements
Must have
• Name of song Title and band name
Nice to have
• Vibe that matches the song / one of our pictures included
Should not have
• any other text

```html
<!DOCTYPE html>
<html lang="en">
<head>
<meta charset="utf-8">
<title>Rain Won't Wait — Orchard 19</title>
<link rel="stylesheet" href="https://fonts.googleapis.com/css2?family=Archivo+Black&family=Montserrat:wght@300&display=swap">
<style>
  :root {
    --ink-white: #ffffff;
    --photo-light: #9a9a9a;
    --photo-mid: #4a4a4a;
    --photo-dark: #141414;
    --photo-deep: #050505;
  }
  html, body {
    margin: 0;
    padding: 0;
    width: 1200px;
    height: 1200px;
    overflow: hidden;
    background: var(--photo-deep);
  }
  .cover {
    position: relative;
    width: 1200px;
    height: 1200px;
    overflow: hidden;
  }
  .cover-photo {
    position: absolute;
    inset: 0;
    background:
      radial-gradient(ellipse 55% 45% at 30% 30%, rgba(255,255,255,0.18), transparent 70%),
      radial-gradient(ellipse 60% 50% at 85% 15%, rgba(255,255,255,0.22), transparent 70%),
      linear-gradient(180deg, var(--photo-light) 0%, var(--photo-mid) 35%, var(--photo-dark) 70%, var(--photo-deep) 100%);
  }
  .title-art {
    position: absolute;
    inset: 0;
    width: 1200px;
    height: 1200px;
  }
  .title-line {
    font-family: "Archivo Black", "Arial Black", sans-serif;
    text-transform: uppercase;
  }
  .title-line--solid { fill: var(--ink-white); opacity: 0.9; }
  .title-line--soft { fill: var(--ink-white); opacity: 0.82; }
  .title-line--outline {
    fill: none;
    stroke: var(--ink-white);
    stroke-width: 3;
  }
  .band-name {
    position: absolute;
    left: 0;
    right: 0;
    top: 1000px;
    margin: 0;
    text-align: center;
    font-family: "Montserrat", "Helvetica Neue", sans-serif;
    font-weight: 300;
    font-size: 84px;
    line-height: 1;
    letter-spacing: 0.42em;
    padding-left: 0.42em;
    color: var(--ink-white);
    text-transform: uppercase;
  }
</style>
</head>
<body>
  <main class="cover">
    <div class="cover-photo" role="img" aria-label="Black and white photo of the duo sitting close together outdoors, leaning heads together and smiling, trees behind them"></div>

    <svg class="title-art" viewBox="0 0 1200 1200" aria-label="Rain Won't Wait" role="img">
      <text class="title-line title-line--solid" x="56" y="320" font-size="340" textLength="1097" lengthAdjust="spacingAndGlyphs">Rain</text>
      <text class="title-line title-line--soft" x="60" y="562" font-size="280" textLength="1080" lengthAdjust="spacingAndGlyphs">Won't</text>
      <text class="title-line title-line--outline" x="56" y="880" font-size="390" textLength="1090" lengthAdjust="spacingAndGlyphs">Wait</text>
    </svg>

    <h1 class="band-name">Orchard 19</h1>
  </main>
</body>
</html>
```